UI/UX Design for AI Photo-to-Video Web Platform (Figma)

I am looking for a modern, high-converting redesign for my Next.js-based web platform. The service allows users to transform old photos into vibrant memories using AI. The design needs to be clean, intuitive, and "mobile-ready" (responsive).
Key Features to Visualize on the Homepage:
Photo Restoration & Colorization: A clear "before/after" visual showing a black-and-white photo turning into a high-quality color photo.
Photo-to-Video Animation: A visual representation of how both B&W and color photos are transformed into dynamic video clips.
Story Creation: A section showing how these photos and videos are combined into a single "Story Video" with background music.
Scope of Work:
Homepage Redesign: A hero section with the core value proposition and a visual walkthrough of the process.
Service/Internal Pages: Redesigning the functional pages where users upload files and manage their projects.
Responsive Design: While the focus is desktop, the layout must be designed with a "Mobile-First" mindset for easy porting to a mobile app later.
Technical Requirements for the Designer:
Tool: Must be designed in Figma.
Structure: Use Figma Auto Layout and Components for all elements (buttons, inputs, cards).
Design System: Provide a clear style guide (Typography, Color Palette, Spacing).
Assets: All icons should be in SVG format.
Style Preference:
Modern, sleek, and trustworthy.
Since the product is about "memories," the vibe should be emotional yet technologically advanced (AI-driven).

```html
<!DOCTYPE html>
<html lang="en">
<head>
<meta charset="utf-8">
<title>Bring Your Old Photos Back To Life</title>
<link href="https://fonts.googleapis.com/css2?family=Inter:wght@400;500;600;700&display=swap" rel="stylesheet">
<style>
:root{
  --bg:#07061a;
  --bg-2:#0d0b26;
  --card:#141236;
  --card-2:#1b1746;
  --line:#2c2762;
  --accent:#6a4cf2;
  --accent-2:#8a6dff;
  --text:#ffffff;
  --muted:#b5b1d6;
  --dim:#8a86b0;
  --star:#f5b83b;
}
*{box-sizing:border-box;margin:0;padding:0}
html,body{width:1200px;height:5286px;overflow:hidden;background:var(--bg)}
body{font-family:"Inter",sans-serif;color:var(--text);position:relative}
.abs{position:absolute}
.page{position:relative;width:1200px;height:5286px;overflow:hidden;
  background:
    radial-gradient(ellipse 700px 400px at 600px 200px,#2a1f6e 0%,transparent 70%),
    radial-gradient(ellipse 500px 400px at 1100px 1800px,#231a5c 0%,transparent 70%),
    radial-gradient(ellipse 600px 300px at 200px 3600px,#1e1750 0%,transparent 70%),
    var(--bg)}
.btn{position:absolute;display:inline-flex;align-items:center;gap:8px;height:40px;padding:0 20px;border:1px solid rgba(255,255,255,.55);border-radius:20px;font-size:12px;color:var(--text);background:rgba(10,8,30,.4)}
.btn svg{width:10px;height:10px}
.ph{position:absolute;border-radius:14px;overflow:hidden}
h2.title{position:absolute;font-size:37px;font-weight:500;line-height:1.2;letter-spacing:-.3px}
.muted{color:var(--muted)}
.small{font-size:12px;line-height:1.55}

/* nav */
.logo{left:72px;top:22px;font-size:28px;font-weight:500;letter-spacing:-.5px}
.nav{left:447px;top:30px;display:flex;gap:0;font-size:12px}
.nav span{position:absolute;white-space:nowrap}
.search{left:1098px;top:22px;width:30px;height:30px;border-radius:50%;background:var(--accent);display:flex;align-items:center;justify-content:center}

/* hero */
.hero-title{left:0;width:1200px;top:134px;text-align:center;font-size:56px;font-weight:500;line-height:1.12;letter-spacing:-.8px}
.hero-sub{left:0;width:1200px;top:273px;text-align:center;font-size:15px}
.strip .ph{box-shadow:0 10px 30px rgba(0,0,0,.5)}
.cap{position:absolute;width:320px;text-align:center}
.cap b{display:block;font-size:13px;font-weight:600;margin-bottom:8px}
.cap p{font-size:11px;color:var(--muted);line-height:1.55}

/* stats band */
.band{left:0;top:815px;width:1200px;height:190px;background:linear-gradient(90deg,#15124a,#2a2178 50%,#15124a);clip-path:polygon(0 18%,100% 0,100% 82%,0 100%)}
.stat{position:absolute;transform:rotate(-2deg)}
.stat b{display:block;font-size:36px;font-weight:500;line-height:1}
.stat span{font-size:21px}

/* about */
.about-h{left:72px;top:1112px;font-size:36px;font-weight:500;line-height:1.2}
.about-p{left:72px;width:340px;font-size:11.5px;line-height:1.65;color:var(--muted)}
.media-card{left:484px;top:1114px;width:302px;height:363px;border-radius:14px;background:linear-gradient(160deg,#3b2c9e,#15123a 60%);border:1px solid var(--line)}
.chip{display:inline-flex;align-items:center;gap:5px;font-size:9.5px;color:var(--muted)}
.tick{width:13px;height:13px;border-radius:50%;background:var(--accent);display:inline-flex;align-items:center;justify-content:center}
.acc-row{position:absolute;left:827px;width:293px;font-size:13px;font-weight:600;display:flex;justify-content:space-between;border-bottom:1px solid var(--line);padding-bottom:12px}
.acc-row i{font-style:normal;color:var(--accent-2);font-weight:400}
.stats-box{left:827px;top:1338px;width:293px;height:133px;border-radius:14px;background:linear-gradient(180deg,#272063,#171440);border:1px solid var(--line)}

/* services */
.svc{position:absolute;border-radius:16px;border:1px solid var(--line);background:linear-gradient(120deg,#16133d,#0f0d2c 60%,#2a1f7a)}
.svc h3{position:absolute;font-size:16px;font-weight:600}
.svc p{position:absolute;font-size:11.5px;line-height:1.5;color:var(--muted)}

/* steps */
.step{position:absolute;top:2298px;width:255px;height:328px;border-radius:12px;overflow:hidden}
.step .lbl{position:absolute;left:14px;bottom:14px;right:14px}
.step .lbl b{display:block;font-size:14px;font-weight:600;line-height:1.3}
.step .lbl span{display:block;font-size:10.5px;line-height:1.45;color:#d9d6f2;margin-top:4px}

/* pricing */
.plan{position:absolute;top:2821px;height:472px;border-radius:14px;background:linear-gradient(180deg,#17143f,#100e2e);border:1px solid var(--line);padding:32px 22px}
.plan h3{font-size:21px;font-weight:500}
.price{margin-top:18px;font-size:36px;color:var(--accent-2);font-weight:500}
.price small{font-size:21px}
.plan p.desc{margin-top:16px;font-size:10.5px;line-height:1.6;color:var(--muted)}
.plan .inc{margin-top:28px;font-size:11.5px;font-weight:500}
.plan ul{list-style:none;margin-top:14px}
.plan li{display:flex;align-items:center;gap:8px;font-size:11px;color:var(--muted);margin-bottom:17px}
.plan .btn{left:22px;bottom:28px}

/* testimonials */
.tband{left:0;top:3390px;width:1200px;height:470px;background:linear-gradient(90deg,#0e0b2c,#1a1550 40%,#2a1c6a 70%,#0e0b2c)}
.quote-card{left:107px;top:3480px;width:287px;height:193px;border-radius:14px;background:linear-gradient(180deg,#221c5c,#171441);border:1px solid var(--line)}
.stars{color:var(--star);font-size:13px;letter-spacing:3px}
.avatar{position:absolute;border-radius:50%;background:linear-gradient(135deg,#c8b9a8,#6e5a4a)}

/* faq */
.faq{position:absolute;left:195px;width:810px;border-radius:10px;background:#1e1a52;border:1px solid var(--line);font-size:12.5px;font-weight:500}
.faq .q{display:flex;justify-content:space-between;padding:0 24px;height:46px;align-items:center}

/* blog */
.post{position:absolute;top:4477px;width:336px;height:335px;border-radius:12px;overflow:hidden;background:#151240}
.post .meta{position:absolute;left:24px;top:242px;font-size:9.5px;color:var(--accent-2)}
.post h4{position:absolute;left:24px;top:262px;font-size:16px;font-weight:600;line-height:1.3;width:280px}

/* footer */
.footer{left:0;top:4904px;width:1200px;height:382px;background:radial-gradient(ellipse 500px 250px at 300px 100px,#1f1858,transparent 70%),#0a0822}
.fcol h5{font-size:12px;font-weight:600;margin-bottom:16px}
.fcol span{display:block;font-size:11px;color:var(--muted);margin-bottom:10px}
.ficon{position:absolute;width:30px;height:30px;border-radius:50%;background:var(--accent);display:flex;align-items:center;justify-content:center}
.contact b{display:block;font-size:12px;font-weight:600}
.contact span{display:block;font-size:10.5px;color:var(--muted);line-height:1.45}
.social{position:absolute;top:5252px;width:20px;height:20px;border-radius:50%;background:var(--accent)}
</style>
</head>
<body>
<div class="page">

<!-- Navigation -->
<div class="abs logo">LOGO</div>
<nav class="abs nav" style="left:0;top:31px;width:1200px;height:16px">
  <span style="left:447px">Home</span>
  <span style="left:525px">About Us</span>
  <span style="left:620px">Features</span>
  <span style="left:711px">How It Works</span>
  <span style="left:826px">Examples</span>
  <span style="left:925px">Pricing</span>
  <span style="left:1008px">Contact Us</span>
</nav>
<div class="abs search"><svg width="14" height="14" viewBox="0 0 24 24" fill="none" stroke="#fff" stroke-width="2.5"><circle cx="11" cy="11" r="7"/><path d="M16 16l5 5"/></svg></div>

<!-- Hero -->
<h1 class="abs hero-title">Bring Your Old Photos<br>Back To Life</h1>
<p class="abs hero-sub muted">Restore, colorize, and turn your memories into cinematic videos using AI.</p>
<a class="btn" style="left:521px;top:315px">Upload Your Photo <svg viewBox="0 0 10 10"><path d="M3 1l4 4-4 4" stroke="#fff" stroke-width="1.6" fill="none"/></svg></a>

<svg class="abs" style="left:380px;top:340px" width="460" height="80" viewBox="0 0 460 80" fill="#fff">
  <path d="M26 30l2 10 10 2-10 2-2 10-2-10-10-2 10-2z"/>
  <path d="M52 14l1 5 5 1-5 1-1 5-1-5-5-1 5-1z"/>
  <path d="M448 30l1.5 7 7 1.5-7 1.5-1.5 7-1.5-7-7-1.5 7-1.5z"/>
  <circle cx="110" cy="40" r="1.5"/><circle cx="150" cy="20" r="1.2"/><circle cx="200" cy="50" r="1.3"/>
  <circle cx="230" cy="14" r="1.5"/><circle cx="260" cy="40" r="1.2"/><circle cx="300" cy="60" r="1.4"/>
  <circle cx="340" cy="26" r="1.2"/><circle cx="380" cy="52" r="1.3"/>
</svg>

<div class="strip">
  <div class="ph" role="img" aria-label="Woman with flowing hair" style="left:-10px;top:394px;width:129px;height:283px;background:linear-gradient(160deg,#8c5a45,#3b2c5a)"></div>
  <div class="ph" role="img" aria-label="Woman in sunglasses under neon light" style="left:144px;top:435px;width:170px;height:201px;background:linear-gradient(150deg,#c43a2f,#3a1030 70%)"></div>
  <div class="ph" role="img" aria-label="Old family portrait" style="left:353px;top:453px;width:143px;height:166px;background:linear-gradient(150deg,#6d6a5e,#2b2a26)"></div>
  <div class="ph" role="img" aria-label="Vintage photo of father and child" style="left:529px;top:453px;width:142px;height:166px;background:linear-gradient(150deg,#9a968c,#3c3a36)"></div>
  <div class="ph" role="img" aria-label="Colorized couple portrait" style="left:704px;top:453px;width:140px;height:166px;background:linear-gradient(150deg,#d8cbb4,#4a3f5e)"></div>
  <div class="ph" role="img" aria-label="Older man in hat and suit" style="left:884px;top:435px;width:170px;height:201px;background:linear-gradient(150deg,#3b5a86,#1b2238)"></div>
  <div class="ph" role="img" aria-label="Street parade with horses" style="left:1083px;top:394px;width:130px;height:283px;background:linear-gradient(160deg,#6e86a8,#8a6a3f)"></div>
</div>

<div class="cap" style="left:113px;top:692px"><b>Photo Restoration &amp; Enhancement</b><p>Restore old, damaged, and faded photos with AI<br>precision.</p></div>
<div class="cap" style="left:440px;top:692px"><b>Colorization &amp; Animation</b><p>Turn black &amp; white photos into vibrant images<br>and animate them into lifelike moments.</p></div>
<div class="cap" style="left:770px;top:692px"><b>Create Story Videos</b><p>Combine photos and clips into emotional videos<br>with music.</p></div>

<!-- Stats band -->
<div class="abs band"></div>
<div class="abs" style="left:0;width:1200px;top:838px;text-align:center;font-size:12px;transform:rotate(-2deg)">Used By 1,200+ Teams Worldwide</div>
<div class="stat" style="left:72px;top:893px"><b>50K+</b><span>Photos Restored</span></div>
<div class="stat" style="left:373px;top:882px"><b>10K+</b><span>Videos Created</span></div>
<div class="stat" style="left:662px;top:870px"><b>30K+</b><span>Happy Users</span></div>
<div class="stat" style="left:923px;top:860px"><b>99%</b><span>Secure Processing</span></div>

<!-- About -->
<h2 class="abs about-h">Reimagining<br>Memories<br>With AI</h2>
<p class="abs about-p" style="top:1262px">We bring your old and faded photos back to life using advanced AI. From restoring damaged details to adding natural color and enhancing clarity, every image is carefully transformed into something vibrant and meaningful.</p>
<p class="abs about-p" style="top:1352px">Go beyond static memories by turning your photos into lifelike animations and cinematic story videos complete with smooth motion and music so you can relive your most important moments in a whole new way.</p>
<a class="btn" style="left:72px;top:1445px">Start Restoring Your Photo <svg viewBox="0 0 10 10"><path d="M3 1l4 4-4 4" stroke="#fff" stroke-width="1.6" fill="none"/></svg></a>

<div class="abs media-card">
  <div class="ph" role="img" aria-label="Before and after restoration of a woman's portrait" style="left:22px;top:22px;width:258px;height:260px;background:linear-gradient(90deg,#6c6c6c 0%,#2a2a2a 50%,#3a2470 50%,#1a103c 100%)"></div>
  <div class="abs" style="left:150px;top:22px;width:2px;height:260px;background:#fff"></div>
  <div class="abs" style="left:141px;top:143px;width:20px;height:20px;border-radius:50%;background:var(--accent)"></div>
  <div class="abs" style="left:30px;top:297px;font-size:15px;font-weight:500">Photo Restoration</div>
  <div class="abs" style="left:30px;top:331px;display:flex;gap:10px">
    <span class="chip"><span class="tick"><svg width="7" height="7" viewBox="0 0 10 10"><path d="M2 5l2 2 4-4" stroke="#fff" stroke-width="1.8" fill="none"/></svg></span>High Resolution Output</span>
    <span class="chip"><span class="tick"><svg width="7" height="7" viewBox="0 0 10 10"><path d="M2 5l2 2 4-4" stroke="#fff" stroke-width="1.8" fill="none"/></svg></span>98% Detail Accuracy</span>
  </div>
</div>

<div class="acc-row" style="top:1109px">Mission <i>—</i></div>
<p class="abs" style="left:827px;top:1157px;width:190px;font-size:10.5px;line-height:1.5;color:var(--muted)">To help people preserve their most valuable memories by restoring, enhancing, and transforming old photos into lifelike visual experiences.</p>
<div class="ph" role="img" aria-label="Colorful portrait of a woman" style="left:1040px;top:1157px;width:80px;height:80px;border-radius:14px;background:linear-gradient(135deg,#2fb8e8,#8a3ad6 50%,#e8a040)"></div>
<div class="abs" style="left:827px;top:1247px;width:16px;height:16px;border-radius:50%;background:var(--accent);display:flex;align-items:center;justify-content:center"><svg width="8" height="8" viewBox="0 0 10 10"><path d="M2 5h6M5 2l3 3-3 3" stroke="#fff" stroke-width="1.6" fill="none"/></svg></div>
<div class="acc-row" style="top:1290px">Vision <i>+</i></div>
<div class="abs stats-box">
  <div class="abs" style="left:18px;top:20px;width:22px;height:22px;border-radius:50%;background:var(--accent-2)"></div>
  <div class="abs" style="left:18px;top:48px;font-size:33px;font-weight:500">230<span style="color:var(--accent-2)">M+</span></div>
  <div class="abs" style="left:18px;top:92px;font-size:10px;color:var(--muted)">Photos Processed</div>
  <div class="abs" style="left:158px;top:20px;width:22px;height:22px;border-radius:50%;background:var(--accent-2)"></div>
  <div class="abs" style="left:158px;top:48px;font-size:33px;font-weight:500">120<span style="color:var(--accent-2)">K+</span></div>
  <div class="abs" style="left:158px;top:92px;font-size:10px;color:var(--muted)">Videos Created</div>
</div>

<!-- Services -->
<h2 class="title" style="left:0;width:1200px;top:1574px;text-align:center">Transform Your Photos Into<br>Living Memories</h2>

<div class="svc" style="left:72px;top:1693px;width:523px;height:185px">
  <div class="ph" role="img" aria-label="Restored vintage family photo" style="left:16px;top:16px;width:248px;height:153px;background:linear-gradient(135deg,#8c6a4a,#3a2a22);border:1px solid var(--line)"></div>
  <h3 style="left:282px;top:22px">Photo Restoration</h3>
  <p style="left:282px;top:48px;width:210px">Restore old, damaged, and faded photos with enhanced clarity and detail.</p>
  <a class="btn" style="left:282px;top:120px;height:34px;font-size:11px">View More <svg viewBox="0 0 10 10"><path d="M3 1l4 4-4 4" stroke="#fff" stroke-width="1.6" fill="none"/></svg></a>
</div>
<div class="svc" style="left:616px;top:1693px;width:512px;height:185px">
  <div class="ph" role="img" aria-label="Colorized portrait of a woman in a garden hat" style="left:16px;top:16px;width:240px;height:153px;background:linear-gradient(135deg,#4c8a8a,#b86a3a 60%,#2a3a2a)"></div>
  <div class="abs" style="left:28px;top:142px;width:216px;font-size:9px;display:flex;justify-content:space-between">Optimization<span>90%</span></div>
  <div class="abs" style="left:28px;top:156px;width:216px;height:3px;background:#555"><div style="width:90%;height:3px;background:#fff"></div></div>
  <h3 style="left:272px;top:28px">Photo Colorization</h3>
  <p style="left:272px;top:54px;width:200px">Turn black &amp; white photos into natural, vibrant colored images.</p>
  <a class="btn" style="left:272px;top:120px;height:34px;font-size:11px">View More <svg viewBox="0 0 10 10"><path d="M3 1l4 4-4 4" stroke="#fff" stroke-width="1.6" fill="none"/></svg></a>
</div>
<div class="svc" style="left:72px;top:1902px;width:605px;height:308px;background:linear-gradient(120deg,#3a2a8a,#16133d 45%,#0f0d2c)">
  <h3 style="left:16px;top:22px">Photo-To-Video Animation</h3>
  <p style="left:16px;top:54px;width:230px">Animate still photos into realistic, lifelike video clips.</p>
  <div class="abs" style="left:16px;top:126px;width:270px;height:104px;border-radius:10px;background:#1b1746"></div>
  <div class="abs" style="left:28px;top:138px;font-size:11px;line-height:30px">
    <div class="chip" style="color:#fff;font-size:11px"><span class="tick"></span>Natural Motion</div><br>
    <div class="chip" style="color:#fff;font-size:11px;margin-top:-18px"><span class="tick"></span>Facial Animation</div><br>
    <div class="chip" style="color:#fff;font-size:11px;margin-top:-18px"><span class="tick"></span>Smooth Transitions</div>
  </div>
  <div class="ph" role="img" aria-label="Small animated scene thumbnail" style="left:184px;top:148px;width:82px;height:62px;border-radius:8px;background:linear-gradient(135deg,#3a8ae0,#e09a3a)"></div>
  <a class="btn" style="left:16px;top:250px;height:36px;font-size:11px">View More <svg viewBox="0 0 10 10"><path d="M3 1l4 4-4 4" stroke="#fff" stroke-width="1.6" fill="none"/></svg></a>
  <div class="ph" role="img" aria-label="Astronaut floating among pastel clouds" style="left:326px;top:18px;width:262px;height:270px;background:linear-gradient(135deg,#d79ad9,#8a9ae8 50%,#3a2a6a)"></div>
  <div class="abs" style="left:440px;top:130px;width:34px;height:34px;border-radius:50%;background:#fff;display:flex;align-items:center;justify-content:center"><svg width="12" height="12" viewBox="0 0 10 10"><path d="M3 2l5 3-5 3z" fill="var(--accent)"/></svg></div>
  <div class="ph" role="img" aria-label="Original still photo" style="left:334px;top:196px;width:72px;height:86px;border-radius:8px;background:linear-gradient(135deg,#9a9aa8,#4a4a5a);border:1px solid #fff"></div>
  <div class="abs" style="left:340px;top:270px;font-size:9px">Your photo</div>
</div>
<div class="svc" style="left:700px;top:1902px;width:428px;height:308px;background:linear-gradient(160deg,#4a3ad0,#16133d 50%,#0f0d2c)">
  <div class="ph" role="img" aria-label="Animated scene of a grandfather and child reading" style="left:16px;top:16px;width:396px;height:196px;background:linear-gradient(135deg,#e0a050,#7a4a2a 60%,#3a2a4a)"></div>
  <h3 style="left:16px;top:232px;font-size:14px">Story Video Creation</h3>
  <p style="left:16px;top:254px;width:260px;font-size:11px">Combine photos and clips into emotional videos with music.</p>
  <a class="btn" style="left:306px;top:238px;height:36px;font-size:11px">View More <svg viewBox="0 0 10 10"><path d="M3 1l4 4-4 4" stroke="#fff" stroke-width="1.6" fill="none"/></svg></a>
</div>

<!-- How it works -->
<h2 class="title" style="left:72px;top:2298px">How It Works</h2>
<p class="abs small muted" style="left:72px;top:2364px;width:250px;font-size:11px">Turn your photos into living memories in just a few simple steps.</p>
<a class="btn" style="left:72px;top:2582px;font-size:11px">Start Creating Your Memory <svg viewBox="0 0 10 10"><path d="M3 1l4 4-4 4" stroke="#fff" stroke-width="1.6" fill="none"/></svg></a>

<div class="step" style="left:340px" role="img" aria-label="Floating app screens for uploading photos">
  <div class="abs" style="inset:0;background:linear-gradient(150deg,#2a2a3a,#111118 60%,#1a1a2a)"></div>
  <div class="lbl"><b>Step 1:<br>Upload Your Photo</b><span>Upload your old or damaged photo in seconds.</span></div>
</div>
<div class="step" style="left:607px" role="img" aria-label="Animated girl meeting a rabbit in a field">
  <div class="abs" style="inset:0;background:linear-gradient(160deg,#8a9a5a,#c89a6a 50%,#5a4a3a)"></div>
  <div class="lbl"><b>Step 2:<br>AI Enhances &amp; Animates</b><span>We restore, colorize, and animate your photo with precision.</span></div>
</div>
<div class="step" style="left:876px" role="img" aria-label="Crow perched among blueberries">
  <div class="abs" style="inset:0;background:linear-gradient(160deg,#6a7a4a,#2a3048 50%,#3a4a7a)"></div>
  <div class="lbl"><b>Step 3:<br>Create Story Video</b><span>Download a cinematic video with music and smooth transitions.</span></div>
</div>

<!-- Pricing -->
<h2 class="title" style="left:0;width:1200px;top:2712px;text-align:center">Simple Pricing For Your Memories</h2>
<p class="abs muted" style="left:0;width:1200px;top:2774px;text-align:center;font-size:13px">Pay only for what you create. No subscriptions required.</p>

<div class="plan" style="left:72px;width:336px">
  <h3>Photo Restore</h3>
  <div class="price">$ 9<small>/Image</small></div>
  <p class="desc">Restore and colorize your old photos with high-quality AI enhancement.</p>
  <div class="inc">Includes:</div>
  <ul><li><span class="tick"></span>Photo Restoration</li><li><span class="tick"></span>Colorization</li><li><span class="tick"></span>High Resolution Output</li></ul>
  <a class="btn" style="font-size:11px">Choose <svg viewBox="0 0 10 10"><path d="M3 1l4 4-4 4" stroke="#fff" stroke-width="1.6" fill="none"/></svg></a>
</div>
<div class="plan" style="left:431px;width:339px;background:radial-gradient(ellipse 250px 200px at 300px 80px,#3a2a8a,transparent 70%),linear-gradient(180deg,#17143f,#100e2e)">
  <h3>Photo Restore</h3>
  <div class="price">$ 19<small>/Video</small></div>
  <p class="desc">Turn your photos into lifelike animated videos with smooth motion and realistic expressions.</p>
  <div class="inc">Includes:</div>
  <ul><li><span class="tick"></span>Photo-to-Video Animation</li><li><span class="tick"></span>Facial Motion Effects</li><li><span class="tick"></span>HD Video Export</li><li><span class="tick"></span>Smooth Transitions</li></ul>
  <a class="btn" style="font-size:11px">Choose <svg viewBox="0 0 10 10"><path d="M3 1l4 4-4 4" stroke="#fff" stroke-width="1.6" fill="none"/></svg></a>
</div>
<div class="plan" style="left:792px;width:336px">
  <h3>Story Pack</h3>
  <div class="price">$ 39<small>/Project</small></div>
  <p class="desc">Create complete story videos by combining multiple photos, animations, and music into one cinematic experience.</p>
  <div class="inc">Includes:</div>
  <ul><li><span class="tick"></span>Multiple Photo Uploads</li><li><span class="tick"></span>Photo-to-Video Animation</li><li><span class="tick"></span>Background Music</li><li><span class="tick"></span>Cinematic Transitions</li><li><span class="tick"></span>Full HD Video Export</li></ul>
  <a class="btn" style="font-size:11px">Choose <svg viewBox="0 0 10 10"><path d="M3 1l4 4-4 4" stroke="#fff" stroke-width="1.6" fill="none"/></svg></a>
</div>

<!-- Testimonials -->
<div class="abs tband"></div>
<div class="abs quote-card">
  <div class="abs stars" style="left:22px;top:22px">★★★★★</div>
  <p class="abs small muted" style="left:22px;top:52px;width:240px;font-size:11px">This brought my family's old photo back to life. Seeing it in color and motion felt truly special.</p>
  <div class="avatar" role="img" aria-label="Customer avatar" style="left:22px;top:130px;width:38px;height:38px"></div>
  <div class="abs" style="left:72px;top:136px;font-size:12px;font-weight:600">Clara N.</div>
  <div class="abs" style="left:72px;top:153px;font-size:9px;color:var(--accent-2)">Verified User</div>
  <div class="abs" style="left:240px;top:140px;font-size:26px;color:var(--accent-2);font-weight:700">”</div>
</div>
<div class="abs" style="left:233px;top:3693px;display:flex;gap:6px"><span style="width:5px;height:5px;border-radius:50%;background:var(--accent-2)"></span><span style="width:5px;height:5px;border-radius:50%;background:#fff"></span><span style="width:5px;height:5px;border-radius:50%;background:#fff"></span></div>
<a class="btn" style="left:107px;top:3745px;font-size:11px">See More Stories <svg viewBox="0 0 10 10"><path d="M3 1l4 4-4 4" stroke="#fff" stroke-width="1.6" fill="none"/></svg></a>
<div class="ph" role="img" aria-label="Portrait of a woman in warm red light" style="left:425px;top:3468px;width:265px;height:318px;background:linear-gradient(150deg,#c8402a,#5a1010 60%,#200808)"></div>
<h2 class="title" style="left:712px;top:3464px">Real Memories,<br>Told By Our Users</h2>
<div class="abs" style="left:712px;top:3570px;display:flex;gap:30px;font-size:11px">
  <span style="padding:0 16px 8px;border-bottom:2px solid #fff">Client Reviews</span>
  <span style="color:var(--accent-2)">Web Review</span>
</div>
<div class="abs" style="left:712px;top:3605px;width:416px;height:1px;background:var(--line)"></div>
<div class="abs stars" style="left:712px;top:3623px">★★★★★</div>
<p class="abs small muted" style="left:712px;top:3652px;width:380px;font-size:11px">People are turning their old photos into emotional memories. From restoring faded images to creating lifelike video stories, our AI helps bring moments back to life in a way that feels real and personal.</p>
<div class="avatar" role="img" aria-label="Customer avatar" style="left:712px;top:3740px;width:52px;height:52px;background:linear-gradient(135deg,#e8e0d8,#8a7a6a)"></div>
<div class="abs" style="left:780px;top:3744px;font-size:12px;font-weight:600">Marcus T.</div>
<div class="abs" style="left:780px;top:3766px;font-size:10px;color:var(--accent-2)">Happy User</div>
<div class="abs" style="left:1058px;top:3744px;font-size:30px;color:var(--accent-2);font-weight:700">”</div>

<!-- FAQ -->
<h2 class="title" style="left:0;width:1200px;top:3948px;text-align:center">Frequently Asked Questions</h2>
<div class="faq" style="top:4018px;height:127px">
  <div class="q">Can I Restore Old And Damaged Photos? <span>—</span></div>
  <div style="margin:0 24px;border-top:1px solid var(--line)"></div>
  <p style="padding:16px 24px;font-size:10.5px;font-weight:400;line-height:1.6;color:var(--muted)">Yes, our AI can repair scratches, enhance clarity, and restore faded or damaged photos with high precision. It carefully improves details, sharpens features, and brings back lost quality, making your old memories look clean, vibrant, and visually appealing.</p>
</div>
<div class="faq" style="top:4161px"><div class="q">Can I Turn A Photo Into A Video? <span>+</span></div></div>
<div class="faq" style="top:4224px"><div class="q">Can I Create A Story Video With Music? <span>+</span></div></div>

<!-- Blog -->
<h2 class="title" style="left:72px;top:4366px">From Our Blog:<br>Memory &amp; AI Stories</h2>
<p class="abs muted" style="left:732px;top:4366px;width:396px;font-size:10.5px;line-height:1.6">Learn how AI is helping people restore old photos, create video memories, and preserve moments that matter most.</p>
<a class="btn" style="left:732px;top:4414px;font-size:11px">Read More Stories <svg viewBox="0 0 10 10"><path d="M3 1l4 4-4 4" stroke="#fff" stroke-width="1.6" fill="none"/></svg></a>

<div class="post" style="left:72px">
  <div class="ph" role="img" aria-label="Smiling woman with curly hair" style="left:0;top:0;width:336px;height:222px;border-radius:0;background:linear-gradient(135deg,#f0ece8,#b8a090)"></div>
  <div class="meta">October 11, 2025 | By Lumera</div>
  <h4>How AI Restores Old Family Photos</h4>
</div>
<div class="post" style="left:431px">
  <div class="ph" role="img" aria-label="Man smiling on a video call" style="left:0;top:0;width:336px;height:222px;border-radius:0;background:linear-gradient(135deg,#e8e8e8,#5a4a3a 60%,#2a2a2a)"></div>
  <div class="meta">October 11, 2025 | By Lumera</div>
  <h4>Turning Old Photos Into Video Memories</h4>
</div>
<div class="post" style="left:792px">
  <div class="ph" role="img" aria-label="Parent hugging a child" style="left:0;top:0;width:336px;height:222px;border-radius:0;background:linear-gradient(135deg,#d8d0c8,#7a5a4a 60%,#3a4a6a)"></div>
  <div class="meta">October 11, 2025 | By Lumera</div>
  <h4>Why Story Videos Feel More Emotional</h4>
</div>

<!-- Footer -->
<footer class="abs footer">
  <div class="abs" style="left:72px;top:70px;font-size:50px;font-weight:500;letter-spacing:-1px">LOGO</div>
  <div class="abs" style="left:72px;top:132px;font-size:17px;font-weight:600;line-height:1.2">Let's Bring Memories<br>Back To Life</div>
  <p class="abs muted" style="left:72px;top:186px;width:240px;font-size:10.5px;line-height:1.55">Bringing your old memories back to life with AI. Restore, colorize, and turn your photos into emotional video stories.</p>
  <div class="abs fcol" style="left:447px;top:82px"><h5>Navigation</h5><span>Home</span><span>Features</span><span>How It Works</span><span>Pricing</span></div>
  <div class="abs fcol" style="left:730px;top:82px"><h5>Quick Link</h5><span>About Us</span><span>Contact</span><span>FAQs</span><span>Privacy Policy</span></div>
  <div class="abs fcol" style="left:1016px;top:82px"><h5>Services</h5><span>Photo Restoration</span><span>Photo Colorization</span><span>Photo-to-Video</span><span>Story Video Creation</span></div>

  <div class="ficon" style="left:447px;top:218px"><svg width="14" height="14" viewBox="0 0 24 24" fill="#fff"><path d="M6.6 10.8a15 15 0 006.6 6.6l2.2-2.2a1 1 0 011-.25 11.4 11.4 0 003.6.6 1 1 0 011 1V20a1 1 0 01-1 1A17 17 0 013 4a1 1 0 011-1h3.5a1 1 0 011 1c0 1.25.2 2.45.6 3.6a1 1 0 01-.25 1z"/></svg></div>
  <div class="abs contact" style="left:497px;top:216px"><b>+1 (555) 014-2290</b><span>Speak with our team for<br>any questions or help.</span></div>
  <div class="ficon" style="left:680px;top:218px"><svg width="14" height="14" viewBox="0 0 24 24" fill="none" stroke="#fff" stroke-width="2"><rect x="3" y="5" width="18" height="14" rx="2"/><path d="M3 7l9 6 9-6"/></svg></div>
  <div class="abs contact" style="left:730px;top:216px"><b>hello@reviva-studio.com</b><span>Reach out via email for<br>support and inquiries.</span></div>
  <div class="ficon" style="left:918px;top:218px"><svg width="14" height="14" viewBox="0 0 24 24" fill="#fff"><path d="M12 2a7 7 0 00-7 7c0 5 7 13 7 13s7-8 7-13a7 7 0 00-7-7zm0 9.5A2.5 2.5 0 1112 6.5a2.5 2.5 0 010 5z"/></svg></div>
  <div class="abs contact" style="left:966px;top:216px"><b>Portland, USA</b><span>Based in the USA,<br>serving users worldwide.</span></div>

  <div class="abs" style="left:72px;top:354px;font-size:10px;color:var(--muted)">© 2026 LOGO. All rights reserved.</div>
</footer>
<div class="social" style="left:1056px"></div>
<div class="social" style="left:1082px"></div>
<div class="social" style="left:1108px"></div>

</div>
</body>
</html>
```